Marrow medical spa and wellness

Integrate existing logo and web design (colors and background) into tri fold, single card brochure and business card design. We already have a logo and an idea for our promotional material but we would like someone to bring it together for us! Quenvoraspaandwellness.com. We want to see what a marble background with a faded lily (as seen on our webpage) would look like on brochures and business cards.

```html
<!DOCTYPE html>
<html lang="en">
<head>
<meta charset="utf-8">
<title>Marrow Medical Spa &amp; Wellness – Business Card</title>
<link rel="stylesheet" href="https://fonts.googleapis.com/css2?family=Dancing+Script:wght@700&family=Jost:wght@400;500&display=swap">
<style>
  :root {
    --page-bg: #1a1a1a;
    --card-bg: #2b2b2c;
    --gold: #c9a237;
    --text-light: #f1f1f1;
    --lily-light: #7d7d7f;
    --lily-dark: #242425;
  }
  * { margin: 0; padding: 0; box-sizing: border-box; }
  html, body {
    width: 1200px;
    height: 800px;
    overflow: hidden;
    background: var(--page-bg);
  }
  .canvas {
    position: relative;
    width: 1200px;
    height: 800px;
  }
  .business-card {
    position: absolute;
    left: 40px;
    top: 84px;
    width: 1120px;
    height: 632px;
    background: var(--card-bg);
    overflow: hidden;
  }
  .brand {
    position: absolute;
    left: 68px;
    top: 110px;
    color: var(--gold);
    font-family: "Jost", sans-serif;
    font-weight: 500;
  }
  .brand-name {
    display: flex;
    align-items: center;
    gap: 14px;
    font-size: 62px;
    line-height: 1;
    letter-spacing: 1px;
  }
  .brand-dot {
    width: 18px;
    height: 18px;
    border-radius: 50%;
    background: var(--gold);
  }
  .brand-tagline {
    margin-top: 10px;
    font-size: 22px;
    letter-spacing: 1.5px;
    text-transform: uppercase;
  }
  .person-name {
    position: absolute;
    left: 68px;
    top: 300px;
    font-family: "Dancing Script", cursive;
    font-weight: 700;
    font-size: 48px;
    color: var(--gold);
  }
  .address {
    position: absolute;
    left: 66px;
    top: 380px;
    font-family: "Jost", sans-serif;
    font-size: 24px;
    line-height: 31px;
    color: var(--text-light);
    font-style: normal;
  }
  .contact-list {
    position: absolute;
    left: 66px;
    top: 457px;
    list-style: none;
    font-family: "Jost", sans-serif;
    font-size: 24px;
    color: var(--text-light);
  }
  .contact-list li {
    display: flex;
    align-items: center;
    gap: 16px;
    height: 32px;
  }
  .contact-icon {
    width: 24px;
    height: 24px;
    fill: var(--gold);
    flex: none;
  }
  .lily-area {
    position: absolute;
    left: 510px;
    top: 60px;
    width: 610px;
    height: 500px;
    background: radial-gradient(ellipse at 45% 45%, var(--lily-light) 0%, #4a4a4c 35%, var(--lily-dark) 72%, var(--card-bg) 100%);
    border-radius: 48% 0 0 40% / 55% 0 0 45%;
  }
</style>
</head>
<body>
<main class="canvas">
  <section class="business-card">
    <div class="brand">
      <div class="brand-name"><span>Marrow</span><span class="brand-dot"></span></div>
      <div class="brand-tagline">Medical Spa &amp; Wellness</div>
    </div>

    <h1 class="person-name">Daniel Harwood</h1>

    <address class="address">
      4120 W. Cedar Lane, Suite 14<br>
      Larkfield, AZ 85390
    </address>

    <ul class="contact-list">
      <li>
        <svg class="contact-icon" viewBox="0 0 24 24" aria-hidden="true"><path d="M6.6 10.8a15.2 15.2 0 0 0 6.6 6.6l2.2-2.2c.3-.3.7-.4 1-.2 1.1.4 2.3.6 3.6.6.6 0 1 .4 1 1V20c0 .6-.4 1-1 1A17 17 0 0 1 3 4c0-.6.4-1 1-1h3.5c.6 0 1 .4 1 1 0 1.3.2 2.5.6 3.6.1.3 0 .7-.2 1z"/></svg>
        <span>(602) 555-0148</span>
      </li>
      <li>
        <svg class="contact-icon" viewBox="0 0 24 24" aria-hidden="true"><path d="M3 6h18v12H3z M3 6l9 7 9-7" fill="none" stroke="#c9a237" stroke-width="2"/></svg>
        <span>welcome@quenvoraspaandwellness.com</span>
      </li>
      <li>
        <svg class="contact-icon" viewBox="0 0 24 24" aria-hidden="true"><circle cx="12" cy="12" r="9" fill="none" stroke="#c9a237" stroke-width="2"/><path d="M3 12h18M12 3c3 3 3 15 0 18M12 3c-3 3-3 15 0 18" fill="none" stroke="#c9a237" stroke-width="1.6"/></svg>
        <span>www.quenvoraspaandwellness.com</span>
      </li>
    </ul>

    <div class="lily-area" role="img" aria-label="Large embossed lily decoration rising from water ripples, in soft grey tones"></div>
  </section>
</main>
</body>
</html>
```